Postcard / Online add graphic

I'm doing a campaign and need a single design that I can put into different formats. I can do that part, I just need the creative part done.

Title: Feed the Social Media Monster with Great Photography
Content: You can take the content from my website: http://www.brindlelenswork.com/business-branding-photography/

Sample Images: https://www.parcelvault.net/sh/k7m2qx9wbtrflzc/QRT3H8k2pwmXcDdLbvHUen_5r?dl=0

Here is a Monster image I licensed for use for this project: https://www.parcelvault.net/s/4hw7ncr2lpzqvkd/stockorbit_xxl_technologymosters.jpg?dl=0

Logo is attached

I want it to be fun, colorful, graphical, and attention getting. Cartoonish is ok.

Target Market(s)

Business owners, social media managers

Industry/Entity Type

Campaign

Font styles to use
Sans Serif

Requirements
Must have
• Title and design on front
• Sales copy on back (whatever fits)
• Contact Information: Wade Pellinger, Photographer, (555) 314-7720, www.brindlelenswork.com

```html
<!DOCTYPE html>
<html lang="en">
<head>
<meta charset="utf-8">
<title>Feed the Social Media Monster – Postcard</title>
<link rel="stylesheet" href="https://fonts.googleapis.com/css2?family=Anton&family=Arvo&family=Baloo+2:wght@800&family=Questrial&family=Roboto+Condensed:ital,wght@0,700;1,400;1,700&display=swap">
<style>
  :root {
    --artboard: #7a7a7a;
    --sky: #6acbe0;
    --sky-band: #3aa6bd;
    --ink: #0d0d0d;
    --paper: #ffffff;
    --coral: #ef5a62;
    --crimson: #b5132e;
    --trim-blue: #2aa8e0;
    --trim-red: #d2203a;
    --copy-blue: #1b7fc4;
    --bubble: #f2f2f2;
  }
  * { margin: 0; padding: 0; box-sizing: border-box; }
  html, body { width: 925px; height: 1200px; overflow: hidden; background: var(--artboard); }
  .canvas { position: relative; width: 925px; height: 1200px; }

  .card { position: absolute; left: 17px; width: 877px; height: 565px; overflow: hidden; }
  .card--front { top: 17px; background: var(--sky); }
  .card--back { top: 602px; background: var(--coral); }
  .trim { position: absolute; inset: 8px; border: 2px solid var(--trim-blue); outline: 2px solid var(--trim-red); outline-offset: 3px; pointer-events: none; z-index: 5; }

  .grid-bands { position: absolute; inset: 0; }

  .monster-art { position: absolute; border-radius: 34px; }
  .monster-art--phone { left: 12px; top: 12px; width: 372px; height: 550px;
    background: linear-gradient(160deg, #f07a7a, #e24b55); border: 16px solid var(--ink); box-shadow: 0 0 0 8px var(--paper); }
  .monster-art--tablet { left: 634px; top: 40px; width: 212px; height: 262px;
    background: linear-gradient(160deg, #6fcbe2, #3fa8c6); border: 12px solid var(--ink); box-shadow: 0 0 0 6px var(--paper); border-radius: 22px; }

  .headline { position: absolute; right: 36px; top: 48px; width: 490px; text-align: right; color: var(--ink);
    text-shadow: 3px 0 0 var(--paper), -3px 0 0 var(--paper), 0 3px 0 var(--paper), 0 -3px 0 var(--paper), 3px 3px 0 var(--paper), -3px -3px 0 var(--paper), 3px -3px 0 var(--paper), -3px 3px 0 var(--paper); }
  .headline__kicker { display: block; text-align: left; font-family: "Anton", sans-serif; font-size: 42px; line-height: 1; font-style: italic; letter-spacing: 0.5px; }
  .headline__main { font-family: "Baloo 2", sans-serif; font-weight: 800; font-size: 80px; line-height: 0.85; letter-spacing: -1px; }
  .headline__main--big { font-size: 90px; }
  .headline__with { font-family: "Anton", sans-serif; font-size: 40px; font-style: italic; }
  .headline__tail { display: block; font-family: "Anton", sans-serif; font-size: 48px; line-height: 1.05; font-style: italic; letter-spacing: 0.5px; margin-top: 4px; }

  .brand { position: absolute; display: flex; align-items: center; gap: 12px;
    font-family: "Questrial", sans-serif; font-size: 34px; letter-spacing: 2px; }
  .brand__dot { width: 18px; height: 18px; border-radius: 50%; }
  .brand--front { left: 410px; top: 478px; color: var(--ink); }
  .brand--front .brand__dot { background: var(--ink); }
  .brand--back { left: 36px; top: 470px; color: var(--paper); }
  .brand--back .brand__dot { background: var(--paper); }

  .backdrop { position: absolute; inset: 0; }
  .pitch { position: absolute; left: 72px; top: 48px; color: var(--copy-blue); }
  .pitch__title { font-family: "Roboto Condensed", sans-serif; font-weight: 700; font-style: italic; font-size: 30px; line-height: 1.1; }
  .pitch__list { list-style: none; margin-top: 6px; margin-left: 58px; font-family: "Roboto Condensed", sans-serif; font-style: italic; font-size: 31px; line-height: 37px; }
  .pitch__list li::before { content: "\2022"; margin-right: 10px; font-size: 20px; vertical-align: middle; }

  .contact { position: absolute; right: 32px; top: 394px; text-align: right; color: var(--paper); font-style: normal; }
  .contact__name { font-family: "Arvo", serif; font-size: 31px; }
  .contact__role { font-family: "Arvo", serif; font-size: 22px; margin-top: 2px; }
  .contact__line { font-family: "Questrial", sans-serif; font-size: 32px; margin-top: 14px; line-height: 1.05; }
  .contact__line + .contact__line { margin-top: 4px; }
</style>
</head>
<body>
<main class="canvas">

  <section class="card card--front" aria-label="Postcard front">
    <svg class="grid-bands" width="877" height="565" viewBox="0 0 877 565" aria-hidden="true">
      <g fill="var(--sky-band)">
        <rect x="380" y="300" width="497" height="16"/>
        <rect x="380" y="390" width="497" height="16"/>
        <rect x="660" y="300" width="16" height="265"/>
        <rect x="800" y="380" width="16" height="185"/>
        <rect x="630" y="190" width="16" height="120"/>
      </g>
    </svg>
    <div class="monster-art monster-art--phone" role="img" aria-label="Cartoon smartphone monster illustration in coral tones"></div>
    <h1 class="headline">
      <span class="headline__kicker">FEED THE</span>
      <span class="headline__main">Social Media</span><br>
      <span class="headline__main headline__main--big">MONSTER</span> <span class="headline__with">with</span>
      <span class="headline__tail">GREAT PHOTOGRAPHY</span>
    </h1>
    <div class="brand brand--front"><span class="brand__dot"></span>Brindle Lenswork</div>
    <div class="trim"></div>
  </section>

  <section class="card card--back" aria-label="Postcard back">
    <svg class="backdrop" width="877" height="565" viewBox="0 0 877 565" aria-hidden="true">
      <path d="M0 395 C120 360 220 410 360 395 S560 340 680 375 S820 360 877 350 L877 565 L0 565 Z" fill="var(--crimson)"/>
      <path d="M0 410 C120 375 220 425 360 410 S560 355 680 390 S820 375 877 365 L877 565 L0 565 Z" fill="var(--ink)"/>
      <path d="M0 382 C120 347 220 397 360 382 S560 327 680 362 S820 347 877 337" fill="none" stroke="var(--ink)" stroke-width="2"/>
      <path d="M40 -20 C15 80 40 200 160 232 C290 264 480 257 565 240 L620 274 L592 205 C640 160 630 40 600 -20 Z" fill="var(--ink)"/>
      <path d="M56 -20 C34 75 58 188 170 217 C290 246 470 242 555 226 L595 248 L578 198 C615 155 608 40 584 -20 Z" fill="var(--bubble)"/>
    </svg>
    <div class="pitch">
      <h2 class="pitch__title">BUSINESS BRANDING PHOTOGRAPHY</h2>
      <ul class="pitch__list">
        <li>Share your story</li>
        <li>Engage your customers</li>
        <li>Sell more products</li>
      </ul>
    </div>
    <div class="monster-art monster-art--tablet" role="img" aria-label="Cartoon tablet monster illustration in blue tones"></div>
    <div class="brand brand--back"><span class="brand__dot"></span>Brindle Lenswork</div>
    <address class="contact">
      <p class="contact__name">Wade Pellinger</p>
      <p class="contact__role">Photographer</p>
      <p class="contact__line">(555) 314-7720</p>
      <p class="contact__line">www.brindlelenswork.com</p>
    </address>
    <div class="trim"></div>
  </section>

</main>
</body>
</html>
```